Restaurant Email Club Sign Up Poster

Looking for a creative design that will catch people's eye and prompt them to sign up for our email club for our Restaurant that we run in Omaha, Nebraska. Open to any creative ways to most effectively grab peoples attention quickly without being too confusing. Want it to be simple but actionable.

Have attached some documents for your assistance - in addition to some marketing materials we have put out in the past.

Would like to put design on posters to hang up throughout the restaurant and likely will make stickers to put on check presenters as well.

Catchy stock photo or use of the cheese curd photo probably good idea - callout things mentioned in the "must haves" section below. Looking for most creative and catchy, yet simple design.

Target Market(s)

30-50 year olds males and females.

Industry/Entity Type

Restaurant

Requirements
Must have
• Must include callouts for -
• Sign up for E-Club for access to future offers and events (or something along these lines)
• Free Appetizer for Signing Up
• Free Birthday Meal
Should not have
• Please do not make this poster like the postcard that I attached to the project - this is not a poster to call out that we are a new burger and beer spot, that we have 40 rotating taps, or that we have 15 specialty burgers, etc. This is simply a poster to grab someones attention and get them to sign up for our email club. Should maybe have a catchy question, something like, "Want a Free Appetizer?" or something catchy and similar, and then below say "And access to future deals and event happenings?"

```html
<!DOCTYPE html>
<html lang="en">
<head>
<meta charset="utf-8">
<title>E-Club Sign Up Poster</title>
<link href="https://fonts.googleapis.com/css2?family=Archivo:wdth,wght@125,700&display=swap" rel="stylesheet">
<style>
  :root {
    --ink: #ffffff;
    --accent: #e0141e;
    --bg-deep: #0c0c0c;
    --bg-mid: #2a2a2a;
    --bg-glow: #4a4a4a;
    --food-light: #f0a040;
    --food-mid: #c8621e;
    --food-dark: #6a2a0c;
  }
  * { margin: 0; padding: 0; box-sizing: border-box; }
  html, body { width: 791px; height: 1200px; overflow: hidden; background: var(--bg-deep); }
  .poster {
    position: relative;
    width: 791px;
    height: 1200px;
    overflow: hidden;
    font-family: "Archivo", Arial, sans-serif;
    font-stretch: 125%;
    font-weight: 700;
    color: var(--ink);
    background:
      radial-gradient(ellipse 60% 45% at 50% 52%, var(--bg-glow) 0%, var(--bg-mid) 45%, var(--bg-deep) 100%);
  }
  .accent { color: var(--accent); }

  .headline {
    position: absolute;
    left: 127px;
    top: 86px;
    font-size: 33px;
    line-height: 34px;
    letter-spacing: 0.5px;
    font-weight: 700;
  }

  .brand {
    position: absolute;
    left: 414px;
    top: 332px;
    width: 114px;
    height: 114px;
    border-radius: 50%;
    background: var(--accent);
    display: flex;
    align-items: center;
    justify-content: center;
    text-align: center;
    font-size: 16px;
    line-height: 19px;
    color: var(--ink);
    z-index: 2;
  }

  .hero-food {
    position: absolute;
    left: 224px;
    top: 478px;
    width: 396px;
    height: 290px;
    border-radius: 44% 46% 40% 42%;
    background: radial-gradient(ellipse at 50% 55%, var(--food-light) 0%, var(--food-mid) 50%, var(--food-dark) 82%, rgba(20,10,5,0) 100%);
  }

  .signup {
    position: absolute;
    left: 338px;
    top: 848px;
    border-left: 4px solid var(--accent);
    padding-left: 9px;
    font-size: 20px;
    line-height: 24px;
    letter-spacing: 0.3px;
  }

  .perks {
    position: absolute;
    left: 60px;
    top: 992px;
    width: 444px;
    border-right: 4px solid var(--accent);
    padding: 12px 12px 12px 0;
    text-align: right;
    font-size: 20px;
    line-height: 28px;
    letter-spacing: 0.3px;
  }
</style>
</head>
<body>
<main class="poster">
  <h1 class="headline">
    <span class="accent">WANT A FREE</span><br>
    Appetizer Today?<br>
    <span class="accent">Join the E-Club</span>
  </h1>

  <div class="brand">Ironhorn<br>Tap</div>

  <div class="hero-food" role="img" aria-label="Photo of golden fried cheese curds with melted cheese"></div>

  <p class="signup">
    <span class="accent">Sign up for</span><br>
    E-Club <span class="accent">for access</span><br>
    <span class="accent">to future</span> offers and events
  </p>

  <p class="perks">
    Free <span class="accent">Appetizer</span> for Signing Up<br>
    Free <span class="accent">Birthday</span> Meal
  </p>
</main>
</body>
</html>
```